Website design for Interior Designer

We want a modern website design for an Interior designer. The website should include completed and undergoing projects, CV, services, news, contact and media gallery pages.

Target Market(s)

People or companies who want to design their properties.

Industry/Entity Type

Interior

Number of Pages Required

5+ page

Requirements
Must have
• Related to interior design.
• Portrait of the designer.
• Her CV.
• Current and completed projects.
• Colours as the attached document.
• Pages mentioned in the description
Nice to have
• Like these websites – but don't copy them😊
• www.pelorandesign.co.za
• www.tamberlinworks.co.za
• www.vkstudioltd.com
• others-
• www.brunoferst.de/en
• www.evadurrant.co.uk/
• Hope that gives you a starting point.

```html
<!DOCTYPE html>
<html lang="en">
<head>
<meta charset="utf-8">
<title>Ines Corbett — Senior Interior Designer</title>
<link rel="stylesheet" href="https://fonts.googleapis.com/css2?family=Questrial&family=Montserrat:wght@700&family=Open+Sans:wght@400&display=swap">
<style>
  :root{
    --ink:#1d1d1d;
    --muted:#9a9a9a;
    --accent:#e8394a;
    --teal:#0ccfbf;
    --yellow:#fff500;
    --footer:#808080;
    --frame:#cfcfcf;
    --white:#ffffff;
    --olive:#a3a06a;
  }
  *{box-sizing:border-box;margin:0;padding:0}
  html,body{width:1200px;height:2359px;overflow:hidden;background:var(--white)}
  body{position:relative;font-family:"Questrial",sans-serif;color:var(--ink)}
  .abs{position:absolute}

  /* header */
  .brand-name{left:117px;top:54px;font-size:28px;color:var(--ink);font-family:"Questrial",sans-serif}
  .brand-role{left:118px;top:94px;font-size:16px;color:var(--ink)}
  .top-phone{right:119px;top:30px;font-size:20px;display:flex;align-items:center;gap:6px}
  .main-nav{right:119px;top:86px;display:flex;gap:25px;font-size:14.5px;text-transform:uppercase}
  .main-nav .current{color:var(--accent)}

  /* hero */
  .hero{left:112px;top:146px;width:973px;height:497px;display:flex;overflow:hidden}
  .hero-panel{height:100%}
  .hero-lounge{width:243px;background:linear-gradient(160deg,#a8946a,#6d6757 55%,#3a4256)}
  .hero-lobby{width:356px;background:linear-gradient(170deg,#b8a184,#d8cdbd 50%,#c08a3a 75%,#3b4f8a)}
  .hero-tower{width:374px;background:linear-gradient(180deg,#9bb6cf,#7d97ad 50%,#d9d2c4 80%,#bdb6aa)}
  .hero-tag{left:154px;top:327px;width:176px;height:44px;background:var(--yellow);font-size:25px;line-height:44px;padding-left:20px;text-transform:uppercase}
  .hero-title{left:156px;top:382px;font-family:"Montserrat",sans-serif;font-weight:700;font-size:44px;line-height:47px;color:var(--white);text-transform:uppercase}
  .hero-dots{left:528px;top:620px;display:flex;gap:6px}
  .hero-dots span{width:24px;height:3px;background:rgba(255,255,255,.7)}
  .hero-dots span.on{background:#222}

  /* about */
  .about-frame-top{left:160px;top:706px;width:194px;height:211px;border:3px solid var(--frame)}
  .about-frame-bottom{left:215px;top:900px;width:195px;height:113px;border:3px solid var(--frame)}
  .about-portrait{left:182px;top:722px;width:244px;height:266px;background:linear-gradient(180deg,#d9d5d2,#8a6a58 55%,#3d3836)}
  .about-title{left:486px;top:724px;font-size:40px;color:var(--accent);text-transform:uppercase;letter-spacing:1px;font-weight:400}
  .about-text{left:486px;top:784px;width:560px;font-family:"Open Sans",sans-serif;font-size:15px;line-height:25px;color:var(--muted)}
  .about-text p+p{margin-top:14px}
  .btn{border:2px solid #555;text-align:center;text-transform:uppercase}
  .read-more{left:491px;top:952px;width:145px;height:39px;line-height:35px;font-size:15px;color:#555}

  /* bands */
  .bands{left:0;top:1004px;width:1200px;height:1206px}

  /* gallery */
  .gallery-btn{left:483px;top:1129px;width:223px;height:48px;line-height:44px;font-size:22px;border-color:var(--white);color:var(--white)}
  .gallery-grid{left:123px;top:1207px;width:955px;height:453px}
  .tile{position:absolute}
  .t1{left:0;top:0;width:243px;height:236px;background:linear-gradient(180deg,#8fb0cc,#6f8aa0 60%,#d8cdb8)}
  .t2{left:243px;top:0;width:356px;height:236px;background:linear-gradient(160deg,#c9b79a,#e2d8c6 50%,#7a6a4c)}
  .t3{left:599px;top:0;width:356px;height:236px;background:linear-gradient(160deg,#e8e6e2,#d7d0c4 60%,#a8a091)}
  .t4{left:0;top:236px;width:350px;height:217px;background:linear-gradient(180deg,#e5e2dc,#7a1f3a 45%,#5a1530)}
  .t5{left:350px;top:236px;width:335px;height:217px;background:linear-gradient(160deg,#8b7a5a,#d6c7aa 50%,#b9aa8f)}
  .t6{left:685px;top:236px;width:270px;height:217px;background:linear-gradient(170deg,#a28f78,#cbbba4 50%,#c08a3a 78%,#3b4f8a)}

  /* contact */
  .contact-btn{left:488px;top:1850px;width:223px;height:47px;line-height:43px;font-size:22px;border-color:var(--ink);color:var(--ink)}
  .contact-text{left:0;top:1914px;width:1200px;text-align:center;font-family:"Open Sans",sans-serif;font-size:14.5px;line-height:25px;color:var(--olive)}
  .contact-line{left:0;width:1200px;display:flex;justify-content:center;align-items:center;gap:8px;font-size:20px}
  .c-addr{top:2011px}.c-phone{top:2051px}.c-mail{top:2090px}

  /* footer */
  .site-footer{left:0;top:2210px;width:1200px;height:149px;background:var(--footer)}
  .foot-nav{left:118px;top:2257px;display:flex;gap:20px;font-size:14.5px;color:var(--white);text-transform:uppercase}
  .foot-copy{left:118px;top:2289px;font-family:"Open Sans",sans-serif;font-size:12.5px;color:#dcdcdc}
  .foot-social{left:892px;top:2250px;display:flex;gap:5px}
  .foot-social span{width:34px;height:34px;border:2px solid var(--white);border-radius:50%}
</style>
</head>
<body>

<header>
  <div class="abs brand-name">Ines Corbett</div>
  <div class="abs brand-role">Senior Interior Designer</div>
  <div class="abs top-phone">
    <svg width="20" height="20" viewBox="0 0 24 24" fill="none" stroke="#e8394a" stroke-width="1.8"><path d="M5 3h4l2 5-2.5 1.5a11 11 0 0 0 6 6L16 13l5 2v4a2 2 0 0 1-2 2A17 17 0 0 1 3 5a2 2 0 0 1 2-2z"/></svg>
    555.014.2280
  </div>
  <nav class="abs main-nav">
    <span class="current">Home</span><span>CV</span><span>Services</span><span>News</span><span>Gallery</span><span>Ongoing Projects</span><span>Contact</span>
  </nav>
</header>

<section class="abs hero">
  <div class="hero-panel hero-lounge" role="img" aria-label="Hotel lounge with white armchairs"></div>
  <div class="hero-panel hero-lobby" role="img" aria-label="Lobby with glass chandelier and orange sofas"></div>
  <div class="hero-panel hero-tower" role="img" aria-label="Glass office tower exterior"></div>
</section>
<div class="abs hero-tag">Welcome</div>
<h1 class="abs hero-title">I'm an interior<br>designer</h1>
<div class="abs hero-dots"><span></span><span></span><span></span><span class="on"></span></div>

<section class="about">
  <div class="abs about-frame-top"></div>
  <div class="abs about-frame-bottom"></div>
  <div class="abs about-portrait" role="img" aria-label="Portrait of the designer"></div>
  <h2 class="abs about-title">About Me</h2>
  <div class="abs about-text">
    <p>Vivamus porttitor purus nisi eleifend libero a tempus libero lectus feugiat felis Morbi diam mauris viverra in gravida eu mattis in ante</p>
    <p>pulvinar metus eget consectetuer augue nisi quis lacus Ut ac mi quis lacus mollis aliquam Curabitur iaculis tempus eros Curabitur vel mi sit amet magna malesuada ultrices Ut nisi erat fermentum vel congue</p>
  </div>
  <div class="abs btn read-more">Read More</div>
</section>

<svg class="abs bands" width="1200" height="1206" viewBox="0 0 1200 1206">
  <polygon points="0,152 1200,0 1200,766 0,703" fill="var(--teal)"/>
  <polygon points="0,703 1200,766 1200,1206 0,1206" fill="var(--yellow)"/>
</svg>

<section class="gallery">
  <div class="abs btn gallery-btn">Gallery</div>
  <div class="abs gallery-grid">
    <div class="tile t1" role="img" aria-label="Office tower exterior"></div>
    <div class="tile t2" role="img" aria-label="Atrium with palm trees"></div>
    <div class="tile t3" role="img" aria-label="Bright atrium with escalators and palms"></div>
    <div class="tile t4" role="img" aria-label="Burgundy room with crystal chandelier and framed art"></div>
    <div class="tile t5" role="img" aria-label="Lobby lounge with palms and seating"></div>
    <div class="tile t6" role="img" aria-label="Lobby with glass chandelier"></div>
  </div>
</section>

<section class="contact">
  <div class="abs btn contact-btn">Contact</div>
  <p class="abs contact-text">Aociosqu ad litora torquent per conubia nostra per inceptos hymenaeos Proin nulla arcu nonummy<br>luctus dictum eget fermentum et lorem Nunc porta convallis pede</p>
  <div class="abs contact-line c-addr">
    <svg width="14" height="20" viewBox="0 0 14 20"><path d="M7 0a7 7 0 0 0-7 7c0 5 7 13 7 13s7-8 7-13a7 7 0 0 0-7-7zm0 10a3 3 0 1 1 0-6 3 3 0 0 1 0 6z" fill="#1d1d1d"/></svg>
    48 Linden Row #4B Austin TX 78701
  </div>
  <div class="abs contact-line c-phone">
    <svg width="18" height="18" viewBox="0 0 24 24" fill="none" stroke="#1d1d1d" stroke-width="1.8"><path d="M5 3h4l2 5-2.5 1.5a11 11 0 0 0 6 6L16 13l5 2v4a2 2 0 0 1-2 2A17 17 0 0 1 3 5a2 2 0 0 1 2-2z"/></svg>
    555.014.2280
  </div>
  <div class="abs contact-line c-mail">
    <svg width="20" height="15" viewBox="0 0 20 15" fill="none" stroke="#1d1d1d" stroke-width="1.6"><rect x="1" y="1" width="18" height="13" rx="1"/><path d="M1 1l9 7 9-7"/></svg>
    hello@inescorbett.com
  </div>
</section>

<footer class="abs site-footer"></footer>
<nav class="abs foot-nav">
  <span>Home</span><span>CV</span><span>Services</span><span>News</span><span>Gallery</span><span>Ongoing Projects</span><span>Contact</span>
</nav>
<p class="abs foot-copy">© 2017 Company Name &nbsp;All right reserved &nbsp;Term of Use</p>
<div class="abs foot-social"><span></span><span></span><span></span><span></span><span></span></div>

</body>
</html>
```